PPT Template Graphic Design for Firm Serving Sales & Mrkting Executives in High-Tech Comopanies

Brookvane seeks a graphic design for a PowerPoint template for corporate presentations.
We are a workforce solutions company that specializes in finding and managing contractors for sales and marketing organizations in high-tech companies. We can also manage entire processes with our 'managed services' solution, for existing clients. We are unique in our exclusive focus on sales & marketing, our consultative approach that works with clients to leverage contractors, not just to fill immediate resource gaps they may have, but also to achieve immediate and longer term business goals of their organization. We offer the dual advantage of flexibility as clients may find within a boutique firm, and the scalability of a global company which means that regardless of whether clients need one contractor or several, locally or in foreign markets, we can help.
We will use this PPT template to present what we do to help clients, and how we are different from the competition to prospective clients. We might also use this PPT template to present proposals.
Updates

Project Deadline Extended
Reason: We would love to see some more design options! Also, we have guaranteed the project since we first posted. Thank you!

Target Market(s)

Executives in sales and marketing organizations of high tech companies, including VP of Sales, VP marketing, CEO, CFO and heads of HR departments.

Industry/Entity Type

Graphic Design

Requirements
Must have
• Template must be simple, elegant, classy. Please include a cover page, supporting pages (for content of presentation) and concluding ("Thank You") page. Design must include our logo & tagline (see attached), and provide recommendations for heading font, copy font and ‘bullet’ styles. Please locate company name on bottom right of template. Design should be in the same family of the look and feel of our website (www.brookvane-example.com). We would like the design to convey simplicity and elegance. We’d also like it to reflect the personality of our firm: friendly and approachable, with a high level of professionalism. Design should feel confident, and up-to-date in its look. Template must be both MAC and PC compatible.
Nice to have
• Same template developed for PPT, imported into a Prezi format as well. We need the PPT template for sure, but one in Prezi would be great to have as well - to enable more professional looking format for presentations.

```html
<!DOCTYPE html>
<html lang="en">
<head>
<meta charset="utf-8">
<title>Brookvane Presentation Template</title>
<link rel="stylesheet" href="https://fonts.googleapis.com/css2?family=Crimson+Text:wght@400;700&family=Fira+Sans:wght@400&display=swap">
<style>
  :root {
    --backdrop: #4a4a4a;
    --slide-light: #fbfbfb;
    --slide-edge: #dcdcdc;
    --brand-orange: #f26b22;
    --accent-blue: #1ea0d8;
    --text-dark: #2b2b2b;
    --text-white: #ffffff;
    --logo-grey: #6d6e71;
  }
  * { box-sizing: border-box; margin: 0; padding: 0; }
  html, body { width: 1200px; height: 849px; overflow: hidden; }
  body { background: var(--backdrop); position: relative; font-family: "Fira Sans", sans-serif; }

  .slide {
    position: absolute; width: 525px; height: 392px;
    background: linear-gradient(100deg, var(--slide-edge) 0%, var(--slide-light) 45%, var(--slide-light) 60%, var(--slide-edge) 100%);
    overflow: hidden;
  }
  .slide--cover { left: 54px; top: 25px; }
  .slide--content { left: 620px; top: 25px; }
  .slide--closing { left: 54px; top: 433px; }

  .hero-panel {
    position: absolute; left: 20px; top: 20px; width: 483px; height: 260px;
    background: var(--brand-orange); border-radius: 6px; color: var(--text-white);
    font-family: "Crimson Text", serif;
  }

  .footer-bar {
    position: absolute; left: 20px; bottom: 0; width: 483px; height: 8px;
    background: var(--accent-blue); border-radius: 4px 4px 0 0;
  }

  .cover-title { position: absolute; left: 26px; top: 74px; font-size: 25px; font-weight: 700; line-height: 33px; }
  .cover-subtitle { position: absolute; left: 26px; top: 164px; font-size: 19px; font-weight: 400; line-height: 25px; }
  .closing-title { position: absolute; left: 27px; top: 110px; font-size: 28px; font-weight: 700; }

  .content-header {
    position: absolute; left: 21px; top: 0; width: 483px; height: 57px;
    background: var(--brand-orange); border-radius: 0 0 6px 6px; color: var(--text-white);
    font-family: "Crimson Text", serif; padding: 8px 0 0 19px;
  }
  .content-header__title { font-size: 19px; font-weight: 700; line-height: 24px; }
  .content-header__subtitle { font-size: 14px; line-height: 18px; }

  .bullet-list { position: absolute; left: 53px; top: 83px; width: 412px; list-style: none; font-size: 12.6px; line-height: 19px; color: var(--text-dark); }
  .bullet-list li { position: relative; }
  .bullet-list li::before {
    content: ""; position: absolute; left: -10px; top: 7px; width: 4px; height: 4px;
    border-radius: 50%; background: var(--accent-blue);
  }
  .bullet-list > li + li { margin-top: 19px; }
  .bullet-list ul { list-style: none; padding-left: 13px; width: 380px; }

  .brand-logo { position: absolute; display: flex; align-items: center; color: var(--logo-grey); }
  .brand-logo__dot { border-radius: 50%; background: var(--brand-orange); flex: none; }
  .brand-logo__name { font-weight: 400; line-height: 1; }

  .brand-logo--large { right: 28px; bottom: 26px; }
  .brand-logo--large .brand-logo__dot { width: 26px; height: 26px; margin-right: 8px; }
  .brand-logo--large .brand-logo__name { font-size: 24px; }
  .brand-logo--small { right: 27px; bottom: 16px; }
  .brand-logo--small .brand-logo__dot { width: 14px; height: 14px; margin-right: 5px; }
  .brand-logo--small .brand-logo__name { font-size: 14px; }

  .social-links { position: absolute; left: 46px; bottom: 23px; display: flex; gap: 5px; list-style: none; }
  .social-links li { width: 23px; height: 23px; border-radius: 3px; background: var(--accent-blue); }
</style>
</head>
<body>
  <section class="slide slide--cover">
    <div class="hero-panel">
      <h1 class="cover-title">Insert The Title of Your<br>Presentation Here</h1>
      <p class="cover-subtitle">Subtitle of the Presentation<br>or<br>main author’s name here</p>
    </div>
    <div class="brand-logo brand-logo--large">
      <span class="brand-logo__dot"></span>
      <span class="brand-logo__name">Brookvane</span>
    </div>
    <div class="footer-bar"></div>
  </section>

  <section class="slide slide--content">
    <header class="content-header">
      <h2 class="content-header__title">Sample Slide - Bullet Points</h2>
      <p class="content-header__subtitle">Placeholder for subtitle</p>
    </header>
    <ul class="bullet-list">
      <li>The text demonstrates how your own text will look when you replace the placeholder with your own text.
        <ul>
          <li>The text demonstrates how your own text will look when you replace the placeholder with your own text.</li>
          <li>The text demonstrates how your own text will look when you replace the placeholder with your own text.</li>
        </ul>
      </li>
      <li>The text demonstrates how your own text will look when you replace the placeholder with your own text.
        <ul>
          <li>The text demonstrates how your own text will look when you replace the placeholder with your own text.</li>
          <li>The text demonstrates how your own text will look when you replace the placeholder with your own text.</li>
        </ul>
      </li>
    </ul>
    <div class="brand-logo brand-logo--small">
      <span class="brand-logo__dot"></span>
      <span class="brand-logo__name">Brookvane</span>
    </div>
    <div class="footer-bar"></div>
  </section>

  <section class="slide slide--closing">
    <div class="hero-panel">
      <h2 class="closing-title">Thank You</h2>
    </div>
    <ul class="social-links" aria-label="Social media links">
      <li></li><li></li><li></li><li></li><li></li>
    </ul>
    <div class="brand-logo brand-logo--large">
      <span class="brand-logo__dot"></span>
      <span class="brand-logo__name">Brookvane</span>
    </div>
    <div class="footer-bar"></div>
  </section>
</body>
</html>
```